Book Cover for College Series

We need an e-book cover design for a collection of poetry entitled, "Chalk Lanterns Vol. 1: The Heartland." Although the price is set to $200, whomever I select for this project will be used for the next three volumes of the series in the future. So be sure to have contact information ready if selected.
If selected, we can be reached at BrightQuillPress@mailnest.example
Be sure to check out the Look and Feel Slider. We would like it to come across as serious and professional, yet very personable and modern.
Target Market(s)
Target market is both current college students as well as former college students (University alums). However, on some level it is marketed towards anyone associated with universities, including professors, as well as poetry readers. Which is why, although personable, We need the look to have a serious feel to it as well.
Industry/Entity Type
College
Requirements
Must have
- The title of the book: "Chalk Lanterns: Vol 1. The Heartland"
- Be sure to have the author's name: Benedict Marlow Tesh
Nice to have
- - Nice to have a design that somehow gives off the feeling of nostalgia.
Optional: Underneath the title, include "A collection of poetry celebrating the top universities of the Midwest."
- Only include the following if it does not get in the way of the feel/look of the cover: Have the initials: B.M.T. on the left-hand corner. An example of how this should appear is in the photo attached However, it does not necessarily need to be this big.

```html
<!DOCTYPE html>
<html lang="en">
<head>
<meta charset="utf-8">
<title>Chalk Lanterns Vol. 1: The Heartland</title>
<link rel="stylesheet" href="https://fonts.googleapis.com/css2?family=Oswald:wght@500&family=Rye&family=Roboto+Condensed:wght@400&display=swap">
<style>
  :root {
    --orange: #f7941e;
    --orange-light: #fba948;
    --orange-deep: #f0871a;
    --brown: #7a2c10;
    --white: #ffffff;
  }
  * { margin: 0; padding: 0; box-sizing: border-box; }
  html, body { width: 900px; height: 1200px; overflow: hidden; background: var(--orange); }
  .cover {
    position: relative;
    width: 900px;
    height: 1200px;
    background: var(--orange);
    overflow: hidden;
  }
  .region-map {
    position: absolute;
    left: 0; top: 0;
    width: 900px; height: 1000px;
    background: radial-gradient(ellipse at 50% 40%, var(--orange-light) 0%, var(--orange) 70%);
    opacity: 0.75;
  }
  .author {
    position: absolute;
    left: 112px; top: 40px;
    font-family: "Oswald", sans-serif;
    font-weight: 500;
    font-size: 28px;
    letter-spacing: 1px;
    color: var(--brown);
    text-transform: uppercase;
  }
  .ornament-band {
    position: absolute;
    left: 96px;
    width: 700px;
    height: 22px;
    background: var(--brown);
  }
  .ornament-band.top { top: 240px; }
  .ornament-band.bottom { top: 376px; }
  .title-art {
    position: absolute;
    left: 0; top: 0;
    width: 900px; height: 1200px;
  }
  .title-main { font-family: "Rye", serif; fill: var(--brown); }
  .title-volume { font-family: "Rye", serif; fill: var(--brown); }
  .title-region { font-family: "Rye", serif; fill: var(--white); }
  .subtitle {
    position: absolute;
    left: 98px; top: 508px;
    width: 700px;
    font-family: "Roboto Condensed", sans-serif;
    font-size: 13.5px;
    letter-spacing: 0.4px;
    color: var(--white);
    text-transform: uppercase;
    white-space: nowrap;
  }
  .initials {
    position: absolute;
    left: 96px; top: 1100px;
    font-family: "Rye", serif;
    font-size: 30px;
    color: var(--brown);
  }
  .compass {
    position: absolute;
    left: 756px; top: 1086px;
    width: 78px; height: 78px;
    border-radius: 50%;
    background: var(--orange-deep);
  }
</style>
</head>
<body>
  <main class="cover">
    <div class="region-map" role="img" aria-label="Faint outline map of the central and northern United States"></div>

    <p class="author">Benedict Marlow Tesh</p>

    <div class="ornament-band top" role="img" aria-label="Decorative ornamental border"></div>

    <svg class="title-art" viewBox="0 0 900 1200" aria-hidden="false">
      <text class="title-main" x="96" y="362" font-size="84" textLength="500" lengthAdjust="spacingAndGlyphs">CHALK LANTERNS</text>
      <text class="title-volume" x="610" y="318" font-size="52" textLength="186" lengthAdjust="spacingAndGlyphs">VOL{1}</text>
      <text class="title-region" x="96" y="492" font-size="88" textLength="700" lengthAdjust="spacingAndGlyphs">THE HEARTLAND</text>
    </svg>

    <div class="ornament-band bottom" role="img" aria-label="Decorative ornamental border"></div>

    <p class="subtitle">A collection of poetry celebrating the top universities of the Midwest.</p>

    <p class="initials">B.M.T.</p>

    <div class="compass" role="img" aria-label="Compass rose emblem"></div>
  </main>
</body>
</html>
```